Design a Travel and Tourism website

We would like a freelancer to design a website that is essentially easy to use and navigate database providing local information for Travelers about destination countries.

We proposed website would discuss different rates, fees, visa requirement, resort locations, cheap flights, etc. This website should be elegant and modern. Our business name is mirdalon.
Some reference websites are plendavix.ca, gosthandiverquo.com,
There should be a forum in the website where travell\ers discuss about their first hand tranvel experience to such destinations.

```html
<!DOCTYPE html>
<html lang="en">
<head>
<meta charset="utf-8">
<title>Mirdalon – Travel &amp; Tourism</title>
<link href="https://fonts.googleapis.com/css2?family=Open+Sans:ital,wght@0,400;0,600;0,700;1,400&family=Raleway:wght@500;600;700&display=swap" rel="stylesheet">
<style>
:root{
  --orange:#e8650f;
  --green:#8dc63f;
  --green-dark:#7ab22f;
  --ink:#2b2b2b;
  --text:#555;
  --muted:#8a8a8a;
  --line:#e2e2e2;
  --panel:rgba(38,38,40,.82);
  --white:#fff;
}
*{box-sizing:border-box;margin:0;padding:0}
html,body{width:1200px;height:2839px;overflow:hidden}
body{position:relative;background:var(--white);font-family:"Open Sans",Arial,sans-serif;color:var(--text);font-size:13px}
svg{display:block}

/* header */
.top-rule{position:absolute;left:0;top:0;width:1200px;height:4px;background:var(--orange)}
.brand{position:absolute;display:flex;align-items:center;gap:10px}
.brand-dot{width:38px;height:38px;border-radius:50%;background:var(--green)}
.brand-name{font-family:"Raleway",sans-serif;font-weight:700;font-size:25px;color:var(--ink);letter-spacing:.5px}
.header-brand{left:91px;top:24px}
.utility{position:absolute;left:412px;top:18px;display:flex;align-items:center;gap:14px;font-size:11.5px;color:#666}
.phone{display:flex;align-items:center;gap:8px;font-family:"Raleway",sans-serif;font-weight:700;font-size:20px;color:var(--ink);margin-right:20px}
.phone-ico{width:26px;height:26px;border:1.5px solid var(--green);border-radius:50%;display:flex;align-items:center;justify-content:center}
.utility .sep{color:#ccc}
.util-link{display:flex;align-items:center;gap:5px}
.util-link i{width:10px;height:9px;background:#888;border-radius:2px;display:inline-block}
.main-nav{position:absolute;right:30px;top:58px;display:flex;gap:22px;font-size:14.5px;color:var(--ink)}
.main-nav .active{display:flex;align-items:center;gap:6px}

/* hero */
.hero{position:absolute;left:0;top:91px;width:1200px;height:509px;
  background:linear-gradient(180deg,#6f8fae 0%,#a9bdcd 35%,#d9d2c0 55%,#7e8d8e 70%,#c9b79a 100%)}
.hero-glow{position:absolute;right:0;top:0;width:360px;height:509px;background:radial-gradient(circle at 80% 60%,#f7a33a 0%,#e06a1a 35%,rgba(120,60,20,0) 75%)}
.hero-arrow{position:absolute;top:330px;color:rgba(255,255,255,.8);font-size:30px}
.search-panel{position:absolute;left:98px;top:127px;width:1002px;height:439px;background:var(--panel);border-radius:6px;color:var(--white)}
.tab{position:absolute;top:25px;height:34px;border:1px solid rgba(255,255,255,.25);background:rgba(255,255,255,.06);border-radius:2px;display:flex;align-items:center;gap:8px;padding-left:10px;font-size:13px;white-space:nowrap}
.tab b{width:16px;height:14px;background:#fff;border-radius:2px;display:inline-block}
.subtabs{position:absolute;left:23px;top:81px;width:632px;height:34px;border:1px solid rgba(255,255,255,.2);display:flex;font-size:13px}
.subtabs span{padding:0 18px;display:flex;align-items:center;white-space:nowrap}
.subtabs .on{background:var(--orange)}
.lbl{position:absolute;font-size:13px;font-weight:600;white-space:nowrap}
.field{position:absolute;height:38px;background:var(--white);border-radius:2px;color:#999;font-size:11.5px;display:flex;align-items:center;gap:8px;padding-left:12px;white-space:nowrap}
.field.select{justify-content:flex-end;padding-right:12px}
.pin{width:9px;height:12px}
.check{position:absolute;left:23px;top:292px;display:flex;align-items:center;gap:9px;font-size:13px;font-weight:600}
.check i{width:13px;height:13px;background:#fff;border-radius:2px}
.adv{position:absolute;left:230px;top:333px;font-size:13px;font-weight:600;white-space:nowrap}
.btn-search{position:absolute;left:23px;top:374px;width:110px;height:46px;border-radius:23px;background:var(--green);border:2px solid #fff;font-weight:700;font-size:14px;display:flex;align-items:center;justify-content:center;letter-spacing:.5px}
.save{position:absolute;left:151px;top:379px;font-size:13.5px;font-weight:700;line-height:22px}

/* features */
.feature{position:absolute;top:634px;display:flex;gap:22px;width:320px}
.feature-ico{width:86px;height:86px;border:1px solid #d6d6d6;border-radius:50%;flex:none;display:flex;align-items:center;justify-content:center}
.feature h3{font-family:"Raleway",sans-serif;font-weight:600;font-size:17px;color:var(--ink);margin:12px 0 8px}
.feature p{font-size:11.5px;line-height:19px;color:#777}
.divider{position:absolute;left:98px;width:1004px;height:1px;background:var(--line)}

.section-title{position:absolute;left:0;width:1200px;text-align:center;font-family:"Raleway",sans-serif;font-weight:700;font-size:28px;color:var(--ink);letter-spacing:.5px}

/* deal cards */
.deal{position:absolute;width:318px;height:333px;border:1px solid #dcdcdc;box-shadow:0 2px 3px rgba(0,0,0,.08);background:#fff}
.deal-photo{height:223px}
.deal h4{font-family:"Raleway",sans-serif;font-weight:600;font-size:17px;color:var(--ink);margin:14px 0 0 16px}
.deal .addr{margin:8px 0 0 16px;font-size:11.5px;color:var(--muted);display:flex;gap:6px;align-items:center;white-space:nowrap}
.deal .rate{margin:8px 0 0 16px;font-size:14px;color:var(--ink)}
.deal .rate strong{color:var(--orange);font-size:21px;font-weight:700}
.btn-more{position:absolute;left:530px;top:1637px;width:140px;height:44px;border:1.5px solid #cfcfcf;border-radius:22px;color:var(--green);font-size:12px;font-weight:700;display:flex;align-items:center;justify-content:center}

/* testimonial */
.testimonial{position:absolute;left:0;top:1738px;width:1200px;height:217px;background:var(--green)}
.quote-mark{position:absolute;left:148px;top:52px;width:112px;height:112px;border-radius:50%;background:#e7e7e7;display:flex;align-items:center;padding-left:20px;font-family:Georgia,serif;font-size:80px;color:#c9c9c9}
.avatar{position:absolute;left:214px;top:50px;width:114px;height:114px;border-radius:50%;border:4px solid #fff;background:linear-gradient(160deg,#e6e6e6,#9aa3ad 60%,#3d4653)}
.testimonial blockquote{position:absolute;left:360px;top:56px;width:700px;font-style:italic;font-size:15px;line-height:30px;color:#fff}
.testimonial cite{position:absolute;left:360px;top:138px;font-style:normal;font-size:17px;color:#fff;font-weight:700}
.testimonial cite em{font-weight:400}
.t-arrow{position:absolute;top:82px;color:rgba(255,255,255,.75);font-size:30px}

/* resorts */
.resort{position:absolute;width:231px;height:184px;border:1px solid #dcdcdc;box-shadow:0 2px 3px rgba(0,0,0,.08);background:#fff}
.resort-photo{height:146px}
.resort-meta{display:flex;justify-content:space-between;padding:9px 10px 0 10px;font-family:"Raleway",sans-serif;font-weight:600;font-size:17px;color:var(--ink)}
.resort-meta span{color:var(--orange);font-weight:700;font-size:15px}

/* footer */
.footer-rule{position:absolute;left:0;top:2528px;width:1200px;height:4px;background:var(--orange)}
.footer-brand{left:91px;top:2620px}
.footer-brand .brand-dot{width:44px;height:44px}
.footer-brand .brand-name{font-size:27px}
.fcol h5{position:absolute;font-family:"Raleway",sans-serif;font-weight:600;font-size:16px;color:var(--ink)}
.flinks{position:absolute;left:396px;top:2603px;list-style:none;font-size:11.5px;color:#666;line-height:27.5px}
.fnote{position:absolute;left:577px;top:2603px;width:250px;font-size:11.5px;line-height:17px;color:#666}
.email-input{position:absolute;left:577px;top:2648px;width:254px;height:36px;border:1px solid #ccc;font-size:11.5px;color:#aaa;padding:10px 12px}
.btn-sub{position:absolute;left:577px;top:2701px;width:95px;height:32px;border-radius:16px;background:var(--green);color:#fff;font-size:10.5px;font-weight:700;display:flex;align-items:center;justify-content:center}
.contact{position:absolute;left:886px;list-style:none;font-size:11.5px;color:#666}
.contact li{position:absolute;left:0;display:flex;gap:14px;width:230px;line-height:19px}
.copyright{position:absolute;left:98px;top:2790px;font-size:11.5px;color:#666}
.cards{position:absolute;left:746px;top:2783px;display:flex;gap:8px}
.cards span{width:50px;height:31px;border-radius:3px;border:1px solid #ccc}
.cards span:nth-child(1){background:#2f78c4}
.cards span:nth-child(2){background:#c92a2a}
.cards span:nth-child(3){background:#f4f4f4}
.social{position:absolute;left:945px;top:2782px;display:flex;gap:8px}
.social span{width:34px;height:34px;border:1.5px solid var(--orange);border-radius:50%}
</style>
</head>
<body>

<div class="top-rule"></div>

<header>
  <div class="brand header-brand"><span class="brand-dot"></span><span class="brand-name">MIRDALON</span></div>
  <div class="utility">
    <span class="phone"><span class="phone-ico"><svg width="12" height="12" viewBox="0 0 24 24"><path d="M6.6 10.8a15 15 0 006.6 6.6l2.2-2.2a1 1 0 011-.25 11 11 0 003.6.6 1 1 0 011 1V20a1 1 0 01-1 1A17 17 0 013 4a1 1 0 011-1h3.5a1 1 0 011 1 11 11 0 00.6 3.6 1 1 0 01-.25 1z" fill="#8dc63f"/></svg></span>1 800 555 0142</span>
    <span class="util-link"><i></i>Credit Card</span><span class="sep">|</span>
    <span class="util-link"><i></i>My Booking</span><span class="sep">|</span>
    <span class="util-link"><i></i>Live Help</span><span class="sep">|</span>
    <span class="util-link"><i></i>Customer Support</span><span class="sep">|</span>
    <span class="util-link"><i></i>Sign In</span>
  </div>
  <nav class="main-nav">
    <span class="active"><svg width="13" height="12" viewBox="0 0 13 12"><path d="M6.5 0L13 6h-2v6H8V8H5v4H2V6H0z" fill="#8dc63f"/></svg>Flights</span>
    <span>Hotels</span><span>Vacation</span><span>Bus</span><span>Car rental</span><span>Vouchers</span><span>Money transfer</span><span>Bill Payment</span>
  </nav>
</header>

<section class="hero" role="img" aria-label="Tropical beach at sunset with palm leaves">
  <div class="hero-glow"></div>
  <span class="hero-arrow" style="left:30px">‹</span>
  <span class="hero-arrow" style="right:30px">›</span>
</section>

<form class="search-panel">
  <span class="tab" style="left:23px;width:87px"><b></b>Flights</span>
  <span class="tab" style="left:121px;width:87px"><b></b>Hotels</span>
  <span class="tab" style="left:220px;width:168px"><b></b>Vacation Packages</span>
  <span class="tab" style="left:401px;width:152px"><b></b>Visa Requirement</span>
  <span class="tab" style="left:564px;width:81px"><b></b>Rates</span>
  <span class="tab" style="left:657px;width:151px"><b></b>Search anything</span>

  <div class="subtabs"><span class="on">Flight + Hotel</span><span style="padding:0 26px">Flight + Hotel + Car</span><span>Flight + Car</span><span style="padding:0 26px">Hotel + Car</span></div>

  <span class="lbl" style="left:23px;top:132px">Flying from</span>
  <span class="lbl" style="left:390px;top:132px">Flying to</span>
  <span class="field" style="left:23px;top:157px;width:354px"><svg class="pin" viewBox="0 0 10 14"><path d="M5 0a5 5 0 015 5c0 4-5 9-5 9S0 9 0 5a5 5 0 015-5z" fill="#666"/></svg>City Or Airport</span>
  <span class="field" style="left:390px;top:157px;width:354px"><svg class="pin" viewBox="0 0 10 14"><path d="M5 0a5 5 0 015 5c0 4-5 9-5 9S0 9 0 5a5 5 0 015-5z" fill="#666"/></svg>City Or Airport</span>

  <span class="lbl" style="left:23px;top:210px">Departing</span>
  <span class="lbl" style="left:221px;top:210px">Returning</span>
  <span class="lbl" style="left:419px;top:210px">Rooms</span>
  <span class="lbl" style="left:511px;top:210px">Adults (18+)</span>
  <span class="lbl" style="left:604px;top:210px">Children (0-17)</span>
  <span class="field" style="left:23px;top:235px;width:187px"><svg width="12" height="12" viewBox="0 0 12 12"><rect x="1" y="2" width="10" height="9" fill="none" stroke="#666"/><path d="M1 5h10" stroke="#666"/></svg>mm/dd/yyyy</span>
  <span class="field" style="left:221px;top:235px;width:187px"><svg width="12" height="12" viewBox="0 0 12 12"><rect x="1" y="2" width="10" height="9" fill="none" stroke="#666"/><path d="M1 5h10" stroke="#666"/></svg>mm/dd/yyyy</span>
  <span class="field select" style="left:419px;top:235px;width:83px"><svg width="9" height="6" viewBox="0 0 9 6"><path d="M1 1l3.5 3.5L8 1" fill="none" stroke="#555" stroke-width="1.4"/></svg></span>
  <span class="field select" style="left:511px;top:235px;width:81px"><svg width="9" height="6" viewBox="0 0 9 6"><path d="M1 1l3.5 3.5L8 1" fill="none" stroke="#555" stroke-width="1.4"/></svg></span>
  <span class="field select" style="left:604px;top:235px;width:81px"><svg width="9" height="6" viewBox="0 0 9 6"><path d="M1 1l3.5 3.5L8 1" fill="none" stroke="#555" stroke-width="1.4"/></svg></span>

  <label class="check"><i></i>I only need a hotel for part of my stay</label>
  <span class="field select" style="left:23px;top:324px;width:189px;justify-content:space-between;padding-left:12px;color:#555">Economy/Coach<svg width="9" height="6" viewBox="0 0 9 6"><path d="M1 1l3.5 3.5L8 1" fill="none" stroke="#555" stroke-width="1.4"/></svg></span>
  <span class="adv">Advanced options ˄</span>
  <span class="btn-search">SEARCH</span>
  <p class="save">SAVE UP TO $433<br>BOOK FLIGHT + HOTEL AT THE SAME TIME*</p>
</form>

<section class="features">
  <div class="feature" style="left:98px">
    <span class="feature-ico"><svg width="30" height="34" viewBox="0 0 30 34"><path d="M7 15v-5a8 8 0 0116 0v5" fill="none" stroke="#e8650f" stroke-width="3.5"/><rect x="2" y="15" width="26" height="19" rx="2" fill="#e8650f"/></svg></span>
    <div><h3>Safe &amp; Secure Booking</h3><p>Nam libero tempore, cum soluta<br>est eligendi optio cum</p></div>
  </div>
  <div class="feature" style="left:449px">
    <span class="feature-ico"><svg width="34" height="32" viewBox="0 0 34 32"><rect x="1" y="13" width="7" height="18" fill="#e8650f"/><path d="M10 14l7-12c3 0 4 2 3.5 5L19 12h11a3 3 0 013 3l-3 14a3 3 0 01-3 2H10z" fill="#e8650f"/></svg></span>
    <div><h3>Buy with Confidence</h3><p>Nam libero tempore, cum soluta<br>est eligendi optio cum</p></div>
  </div>
  <div class="feature" style="left:806px">
    <span class="feature-ico"><svg width="36" height="32" viewBox="0 0 36 32"><path d="M2 4h14l18 18-10 10L6 14z" fill="#e8650f" transform="rotate(-8 18 16)"/><circle cx="10" cy="10" r="2.5" fill="#fff"/></svg></span>
    <div><h3>Low Fare Promise</h3><p>Nam libero tempore, cum soluta<br>est eligendi optio cum</p></div>
  </div>
</section>

<div class="divider" style="top:763px"></div>

<h2 class="section-title" style="top:824px">TOP DEALS</h2>

<section class="deals">
  <article class="deal" style="left:98px;top:899px"><div class="deal-photo" role="img" aria-label="Resort pavilion lit at dusk beside a pool" style="background:linear-gradient(180deg,#3d5b86,#243d5e 55%,#c58a3e)"></div><h4>Verano Hotel</h4><p class="addr"><svg class="pin" viewBox="0 0 10 14"><path d="M5 0a5 5 0 015 5c0 4-5 9-5 9S0 9 0 5a5 5 0 015-5z" fill="#aaa"/></svg>212 Harbor Ave / Cheap Hotel in Los Angeles</p><p class="rate">From <strong>$55</strong> avg. nightly rate</p></article>
  <article class="deal" style="left:441px;top:899px"><div class="deal-photo" role="img" aria-label="Villa terrace with lounge pergola and pool" style="background:linear-gradient(180deg,#9fc3e0,#d9d4c6 50%,#3ab5cf)"></div><h4>Verano Hotel</h4><p class="addr"><svg class="pin" viewBox="0 0 10 14"><path d="M5 0a5 5 0 015 5c0 4-5 9-5 9S0 9 0 5a5 5 0 015-5z" fill="#aaa"/></svg>212 Harbor Ave / Cheap Hotel in Los Angeles</p><p class="rate">From <strong>$55</strong> avg. nightly rate</p></article>
  <article class="deal" style="left:784px;top:899px"><div class="deal-photo" role="img" aria-label="Modern villa with infinity pool facing the sea" style="background:linear-gradient(180deg,#5f8fc2,#a7bfd6 45%,#3a6a88 75%,#2e3d4a)"></div><h4>Verano Hotel</h4><p class="addr"><svg class="pin" viewBox="0 0 10 14"><path d="M5 0a5 5 0 015 5c0 4-5 9-5 9S0 9 0 5a5 5 0 015-5z" fill="#aaa"/></svg>212 Harbor Ave / Cheap Hotel in Los Angeles</p><p class="rate">From <strong>$55</strong> avg. nightly rate</p></article>
  <article class="deal" style="left:98px;top:1261px"><div class="deal-photo" role="img" aria-label="White lakeside palace under hazy hills" style="background:linear-gradient(180deg,#c9c6c2,#aeb0b0 45%,#9fa9ad 70%,#6f7f86)"></div><h4>Verano Hotel</h4><p class="addr"><svg class="pin" viewBox="0 0 10 14"><path d="M5 0a5 5 0 015 5c0 4-5 9-5 9S0 9 0 5a5 5 0 015-5z" fill="#aaa"/></svg>212 Harbor Ave / Cheap Hotel in Los Angeles</p><p class="rate">From <strong>$55</strong> avg. nightly rate</p></article>
  <article class="deal" style="left:441px;top:1261px"><div class="deal-photo" role="img" aria-label="Palm-lined pool by the ocean" style="background:linear-gradient(180deg,#4f8fd0,#a8cbe3 45%,#2d6a45 62%,#35b6c9)"></div><h4>Verano Hotel</h4><p class="addr"><svg class="pin" viewBox="0 0 10 14"><path d="M5 0a5 5 0 015 5c0 4-5 9-5 9S0 9 0 5a5 5 0 015-5z" fill="#aaa"/></svg>212 Harbor Ave / Cheap Hotel in Los Angeles</p><p class="rate">From <strong>$55</strong> avg. nightly rate</p></article>
  <article class="deal" style="left:784px;top:1261px"><div class="deal-photo" role="img" aria-label="Historic waterfront hotel with boats in the harbour" style="background:linear-gradient(180deg,#2f7fd0,#86b8e4 45%,#c5a77e 65%,#2f6f8f)"></div><h4>Verano Hotel</h4><p class="addr"><svg class="pin" viewBox="0 0 10 14"><path d="M5 0a5 5 0 015 5c0 4-5 9-5 9S0 9 0 5a5 5 0 015-5z" fill="#aaa"/></svg>212 Harbor Ave / Cheap Hotel in Los Angeles</p><p class="rate">From <strong>$55</strong> avg. nightly rate</p></article>
</section>

<span class="btn-more">VIEW MORE &gt;&gt;</span>

<section class="testimonial">
  <span class="t-arrow" style="left:100px">‹</span>
  <span class="t-arrow" style="left:1080px">›</span>
  <span class="quote-mark">“</span>
  <span class="avatar" role="img" aria-label="Portrait of the reviewer"></span>
  <blockquote>"...At vero eos et accusamus et iusto odio dignissimos ducimus qui blanditiis praesentium voluptatum deleniti atque corrupti quos dolores et quas molestias excepturi sint occaecati, similiqu...."</blockquote>
  <cite>Daniel Morrow, <em>London</em></cite>
</section>

<h2 class="section-title" style="top:2009px">RESORT LOCATIONS</h2>

<section class="resorts">
  <article class="resort" style="left:98px;top:2082px"><div class="resort-photo" role="img" aria-label="Harbour city seen from above" style="background:linear-gradient(180deg,#7fb3e0,#3d8fc4 50%,#2f6e96)"></div><p class="resort-meta">Australia<span>$495</span></p></article>
  <article class="resort" style="left:356px;top:2082px"><div class="resort-photo" role="img" aria-label="Mountain lake with driftwood" style="background:linear-gradient(180deg,#b8c8d6,#5e7590 40%,#4aa7b0 70%,#b29a7a)"></div><p class="resort-meta">Canada<span>$370</span></p></article>
  <article class="resort" style="left:613px;top:2082px"><div class="resort-photo" role="img" aria-label="Palm tree and deck chairs on a white beach" style="background:linear-gradient(180deg,#2f8fd8,#6cc3e8 50%,#e9e1cf)"></div><p class="resort-meta">Caribbean<span>$310</span></p></article>
  <article class="resort" style="left:871px;top:2082px"><div class="resort-photo" role="img" aria-label="Terraced coastline at golden hour" style="background:linear-gradient(180deg,#2c4e6e,#5a7a8a 40%,#b08a52 70%,#3c3a30)"></div><p class="resort-meta">Far East<span>$420</span></p></article>
  <article class="resort" style="left:98px;top:2283px"><div class="resort-photo" role="img" aria-label="Old city tower lit at twilight" style="background:linear-gradient(180deg,#3e4f9a,#6a70b4 45%,#d9925a 75%,#5a3e4e)"></div><p class="resort-meta">Middle East<span>$290</span></p></article>
  <article class="resort" style="left:356px;top:2283px"><div class="resort-photo" role="img" aria-label="Lupin flowers by a lake and mountains" style="background:linear-gradient(180deg,#5f9ad8,#7aa6c4 40%,#8d6aa8 70%,#4f7a3e)"></div><p class="resort-meta">New Zealand<span>$580</span></p></article>
  <article class="resort" style="left:613px;top:2283px"><div class="resort-photo" role="img" aria-label="City skyline with bridge at dusk" style="background:linear-gradient(180deg,#5f7ab0,#8fa0c4 45%,#4e5d80 75%,#2c3550)"></div><p class="resort-meta">South Africa<span>$480</span></p></article>
  <article class="resort" style="left:871px;top:2283px"><div class="resort-photo" role="img" aria-label="Rainforest waterfall" style="background:linear-gradient(180deg,#2e4a22,#4e7a2e 45%,#8fb84a 65%,#23391a)"></div><p class="resort-meta">South America<span>$420</span></p></article>
</section>

<footer>
  <div class="footer-rule"></div>
  <div class="brand footer-brand"><span class="brand-dot"></span><span class="brand-name">MIRDALON</span></div>
  <div class="fcol">
    <h5 style="left:396px;top:2566px">Quick Links</h5>
    <h5 style="left:577px;top:2566px">Newsletter Subscription</h5>
    <h5 style="left:886px;top:2566px">Contact Us</h5>
  </div>
  <ul class="flinks"><li>About Us</li><li>Contact Us</li><li>Terms and Conditions</li><li>Privacy Policy</li><li>FAQ</li></ul>
  <p class="fnote">Register your Email Address to get information about us</p>
  <div class="email-input">Email Address</div>
  <span class="btn-sub">SUBSCRIBE</span>
  <ul class="contact">
    <li style="top:2603px"><svg class="pin" viewBox="0 0 10 14" style="flex:none;margin-top:3px"><path d="M5 0a5 5 0 015 5c0 4-5 9-5 9S0 9 0 5a5 5 0 015-5z" fill="#e8650f"/></svg>18 Elmfield Court, 7 Brookside Lane, Ashvale, AV2 9KL</li>
    <li style="top:2667px"><svg width="12" height="12" viewBox="0 0 24 24" style="flex:none;margin-top:3px"><path d="M6.6 10.8a15 15 0 006.6 6.6l2.2-2.2a1 1 0 011-.25 11 11 0 003.6.6 1 1 0 011 1V20a1 1 0 01-1 1A17 17 0 013 4a1 1 0 011-1h3.5a1 1 0 011 1 11 11 0 00.6 3.6 1 1 0 01-.25 1z" fill="#e8650f"/></svg>1 800 555 0142</li>
    <li style="top:2710px"><svg width="13" height="10" viewBox="0 0 13 10" style="flex:none;margin-top:4px"><rect width="13" height="10" rx="1" fill="#e8650f"/><path d="M0 1l6.5 5L13 1" fill="none" stroke="#fff"/></svg>info@mirdalon.com</li>
  </ul>
  <div class="divider" style="top:2767px"></div>
  <p class="copyright">Copyright © 2017, Mirdalon. All rights reserved</p>
  <div class="cards"><span></span><span></span><span></span></div>
  <div class="social"><span></span><span></span><span></span><span></span></div>
</footer>

</body>
</html>
```